Australian IT Company requires Business Card Design

Bluepeak is an Australian company that specialises in IT consulting & support, software development, project management, network services.

We have been in business for 15 years.

* We require a business card with the following on it:
Logo
Address
Contact Details
Space for staff name, title & mobile number

Industry/Entity Type

Software

```html
<!DOCTYPE html>
<html lang="en">
<head>
<meta charset="utf-8">
<title>Bluepeak Business Card</title>
<link href="https://fonts.googleapis.com/css2?family=Montserrat:wght@700&family=Open+Sans:wght@400;600&display=swap" rel="stylesheet">
<style>
  :root {
    --brand-blue: #3a6f9c;
    --brand-blue-dark: #2d5a86;
    --slate-grey: #6b7177;
    --ink: #222a31;
    --paper: #ffffff;
    --backdrop: #e9ebee;
  }
  * { margin: 0; padding: 0; box-sizing: border-box; }
  html, body { width: 1200px; height: 900px; overflow: hidden; }
  body {
    background: var(--backdrop);
    font-family: "Open Sans", Arial, sans-serif;
    color: var(--ink);
    position: relative;
  }
  .card {
    position: absolute;
    left: 270px;
    width: 660px;
    height: 378px;
    border-radius: 22px;
    overflow: hidden;
    box-shadow: 0 6px 18px rgba(0,0,0,0.12);
  }
  .card-front { top: 51px; background: var(--paper); }
  .card-back { top: 471px; background: var(--brand-blue); }

  .wordmark { display: flex; align-items: center; gap: 10px; }
  .wordmark-square { width: 26px; height: 26px; background: var(--brand-blue-dark); }
  .wordmark-name {
    font-family: "Montserrat", Arial, sans-serif;
    font-weight: 700;
    font-size: 32px;
    letter-spacing: 0.5px;
    color: var(--brand-blue-dark);
  }
  .tagline {
    font-size: 10px;
    letter-spacing: 3px;
    text-transform: uppercase;
    color: var(--slate-grey);
    margin-top: 4px;
    margin-left: 36px;
  }

  .front-brand { position: absolute; left: 40px; top: 50px; }
  .swoosh { position: absolute; left: 0; bottom: 0; width: 660px; height: 220px; }
  .front-web {
    position: absolute;
    left: 46px;
    bottom: 34px;
    font-size: 15px;
    letter-spacing: 3px;
    color: var(--paper);
  }

  .contact { position: absolute; left: 420px; top: 46px; font-size: 13.5px; line-height: 1.4; }
  .contact-name { font-size: 20px; color: var(--brand-blue-dark); font-weight: 400; }
  .contact-title { margin-bottom: 10px; }
  .contact-address { margin-bottom: 8px; }
  .contact-line { display: flex; align-items: center; gap: 7px; }
  .contact-icon { width: 13px; height: 13px; flex: none; }

  .back-brand { position: absolute; left: 140px; top: 118px; }
  .back-brand .wordmark-square { background: var(--paper); width: 34px; height: 34px; }
  .back-brand .wordmark-name { color: var(--paper); font-size: 46px; }
  .back-brand .tagline { color: #dfe8f0; font-size: 12px; margin-left: 46px; letter-spacing: 4px; }
  .back-web {
    position: absolute;
    left: 140px;
    top: 250px;
    font-size: 17px;
    letter-spacing: 5px;
    color: var(--paper);
  }
</style>
</head>
<body>

<section class="card card-front">
  <div class="front-brand">
    <div class="wordmark">
      <span class="wordmark-square"></span>
      <span class="wordmark-name">BLUEPEAK</span>
    </div>
    <p class="tagline">Dependable technology partners</p>
  </div>

  <svg class="swoosh" viewBox="0 0 660 220" aria-hidden="true">
    <path d="M0 50 C160 75 370 145 600 220" fill="none" stroke="var(--slate-grey)" stroke-width="5"/>
    <path d="M0 68 C160 95 360 160 560 220 L0 220 Z" fill="var(--brand-blue)"/>
  </svg>
  <p class="front-web">www.bluepeak.net.au</p>

  <div class="contact">
    <p class="contact-name">Liam Harcourt</p>
    <p class="contact-title">Manager</p>
    <p class="contact-address">14 Ridge Lane<br>Unit 3<br>Carlton Vic 3053</p>
    <p class="contact-line">
      <svg class="contact-icon" viewBox="0 0 16 16" aria-hidden="true"><path d="M4 1 L6 5 L4.5 6.5 C5.5 8.5 7.5 10.5 9.5 11.5 L11 10 L15 12 L13.5 15 C7 14 2 9 1 2.5 Z" fill="var(--brand-blue-dark)"/></svg>
      +61 3 9555 0182
    </p>
    <p class="contact-line">
      <svg class="contact-icon" viewBox="0 0 16 16" aria-hidden="true"><rect x="4" y="1" width="8" height="14" rx="1.5" fill="none" stroke="var(--brand-blue-dark)" stroke-width="1.6"/><circle cx="8" cy="12.5" r="1" fill="var(--brand-blue-dark)"/></svg>
      +61 3 9555 0100
    </p>
    <p class="contact-line">
      <svg class="contact-icon" viewBox="0 0 16 16" aria-hidden="true"><rect x="1" y="3" width="14" height="10" rx="1" fill="none" stroke="var(--brand-blue-dark)" stroke-width="1.6"/><path d="M1.5 3.5 L8 9 L14.5 3.5" fill="none" stroke="var(--brand-blue-dark)" stroke-width="1.6"/></svg>
      liam@bluepeak.net.au
    </p>
  </div>
</section>

<section class="card card-back">
  <div class="back-brand">
    <div class="wordmark">
      <span class="wordmark-square"></span>
      <span class="wordmark-name">BLUEPEAK</span>
    </div>
    <p class="tagline">Dependable technology partners</p>
  </div>
  <p class="back-web">www.bluepeak.net.au</p>
</section>

</body>
</html>
```